DesertCrown.Com Website Design

We need a logo with website designed for the domain desertcrown.com. This is a domain that will be a tribute domain for the ruler of Saudi Arabia. For reference you can see how palmfalconer.com looks and do something similar. The site will need to be easily updateable. We will be adding news and content regularly so it will need to be a very content friendly site. We may even use word-press as the site management tool. We've uploaded the site map in the pdf that's attached along with some images that you can use for the site. Design needs to be per the sitemap. Please feel free to edit the images I've uploaded also use stock images if required.

Industry/Entity Type

Domain

Number of Pages Required

5+ page

Requirements
Must have
• Design has to be per the sitemap attached.

```html
<!DOCTYPE html>
<html lang="en">
<head>
<meta charset="utf-8">
<title>DesertCrown.Com</title>
<link href="https://fonts.googleapis.com/css2?family=Montserrat:wght@400;600;700&family=Open+Sans:wght@400;600;700&display=swap" rel="stylesheet">
<style>
:root{
  --gold:#d4a21f;
  --dark:#1d1d1f;
  --darker:#151516;
  --grey-bg:#ececec;
  --white:#ffffff;
  --text-muted:#9a9a9a;
  --green:#1f6b4a;
  --violet:#4a4a7c;
  --heading:"Montserrat",sans-serif;
  --body:"Open Sans",sans-serif;
}
*{box-sizing:border-box;margin:0;padding:0}
html,body{width:1200px;height:2872px;overflow:hidden}
body{position:relative;background:var(--white);font-family:var(--body);color:#333}
.abs{position:absolute}
.btn{display:inline-block;background:var(--gold);color:var(--white);font:600 13px var(--body);padding:9px 20px}

/* header */
.hero{left:0;top:0;width:1200px;height:720px;background:linear-gradient(180deg,#3b3128 0%,#6b5640 45%,#3a2f27 100%)}
.site-header{left:0;top:0;width:1200px;height:72px;background:rgba(20,20,20,.85);display:flex;align-items:center;padding:0 64px;z-index:2}
.brand{font:700 30px var(--heading);color:var(--white);letter-spacing:1px}
.main-nav{margin-left:auto;display:flex;gap:34px;font:600 13px var(--heading);color:var(--white)}
.main-nav .active{color:var(--gold)}
.hero-tag{left:668px;top:346px;z-index:2;background:rgba(0,0,0,.6);color:var(--gold);font:600 11px var(--body);padding:5px 12px}
.hero-title{left:100px;top:384px;width:1000px;z-index:2;text-align:center;font:700 36px/50px var(--heading);color:var(--white);text-transform:uppercase}

/* content band */
.content-band{left:0;top:720px;width:1200px;height:1200px;background:var(--grey-bg)}
.card-dark{left:100px;top:784px;width:320px;height:436px;background:var(--dark);padding:24px}
.card-dark h3{font:700 17px/24px var(--heading);color:var(--white);text-transform:uppercase}
.mini{display:flex;gap:14px;margin-top:24px}
.mini .thumb{width:140px;height:92px;flex:none}
.mini p{font:12px/17px var(--body);color:#ccc}
.mini span{display:block;color:var(--gold);font-size:11px;margin-top:6px}
.pager{position:absolute;right:24px;bottom:22px;display:flex;gap:6px}
.pager i{width:14px;height:14px;border:1px solid #777;display:block}

.story{left:432px;top:784px;width:380px;height:436px;background:linear-gradient(160deg,#8a6a4b,#4c3b2f 60%,#2a221d)}
.story-text{left:462px;top:958px;width:340px}
.story-text h2{font:700 30px/36px var(--heading);color:var(--white);text-transform:uppercase}
.story-text .btn{margin-top:86px}

.newsletter{left:828px;top:784px;width:272px;height:196px;background:var(--violet);padding:22px}
.newsletter h4{font:700 16px var(--heading);color:var(--white);text-transform:uppercase}
.newsletter p{font:12px/17px var(--body);color:#ddd;margin-top:8px}
.newsletter .field{margin-top:12px;height:30px;background:var(--white)}
.newsletter .btn{margin-top:12px}
.national{left:828px;top:1000px;width:272px;height:88px;background:#0c0c0c;display:flex;align-items:center;justify-content:center;font:600 22px var(--heading);color:var(--white)}
.quotes{left:828px;top:1104px;width:272px;height:116px;background:var(--green);padding:16px 20px}
.quotes h4{font:700 16px var(--heading);color:var(--white)}
.quotes p{font:12px/17px var(--body);color:#e4efe9;margin-top:8px}

.projects{left:100px;top:1288px;width:580px;height:592px;background:linear-gradient(170deg,#a88d70,#6a5644 50%,#2f2821)}
.projects-text{left:132px;top:1560px;width:520px}
.projects-text h2{font:700 30px var(--heading);color:var(--white);text-transform:uppercase;white-space:nowrap}
.projects-text p{font:13px/19px var(--body);color:#e6e6e6;margin-top:12px}
.projects-text .btn{margin-top:22px}

.orgs{left:700px;top:1288px;width:400px;height:240px;background:linear-gradient(160deg,#5b67a8,#3a4680);padding:22px}
.orgs h3{font:700 19px var(--heading);color:var(--white);text-transform:uppercase}
.orgs p{font:12px/17px var(--body);color:#e6e8f4;margin-top:10px;width:340px}
.orgs .btn{margin-top:18px}

.social{left:700px;top:1552px;width:400px;height:328px;background:#f7f7f7;padding:20px 28px}
.social h3{font:600 22px var(--heading);color:#555;text-align:center}
.tweets{display:flex;gap:22px;margin-top:28px}
.tweet{flex:1;display:flex;gap:10px}
.avatar{width:34px;height:34px;border-radius:50%;background:#b89a7a;flex:none}
.tweet p{font:11px/16px var(--body);color:#777}
.tweet b{display:block;margin-top:8px;color:var(--gold);font:600 12px var(--body)}
.dots{display:flex;gap:8px;justify-content:center;margin-top:36px}
.dots i{width:9px;height:9px;border-radius:50%;background:#ccc;display:block}
.dots i:first-child{background:var(--gold)}

/* video */
.video-band{left:0;top:1920px;width:1200px;height:500px;background:var(--darker)}
.video{left:248px;top:1988px;width:704px;height:372px;background:linear-gradient(180deg,#7b8a96,#4d5863 55%,#2d3338)}
.video-title{left:248px;top:2044px;width:704px;text-align:center;font:700 60px var(--heading);color:var(--white)}
.play{left:535px;top:2150px}

/* footer */
.site-footer{left:0;top:2420px;width:1200px;height:452px;background:var(--dark)}
.fcol{top:2470px}
.fcol h5{font:700 16px var(--heading);color:var(--white);text-transform:uppercase;margin-bottom:14px}
.fcol .lead{font:600 16px var(--body);color:var(--gold);margin:10px 0 6px}
.fcol p{font:12px/17px var(--body);color:var(--text-muted);width:330px}
.fcol ul{list-style:none;margin-top:4px}
.fcol li{font:13px/21px var(--body);color:#bbb}
.fcol.company li{color:var(--gold);font-size:15px;line-height:25px}
.footer-bar{left:0;top:2812px;width:1200px;height:60px;background:#111;display:flex;align-items:center;padding:0 100px;font:12px var(--body);color:var(--text-muted)}
.footer-bar .legal{margin-left:auto;display:flex;gap:40px}
</style>
</head>
<body>

<div class="abs hero" role="img" aria-label="Photo of the prince standing at his office desk with flags and drapes"></div>
<header class="abs site-header">
  <div class="brand">DESERTCROWN</div>
  <nav class="main-nav"><span class="active">HOME</span><span>NEWS ▾</span><span>ABOUT ▾</span><span>CAREER ▾</span><span>FOUNDATIONS AND ACTIVITIES ▾</span><span>MEDIA ▾</span></nav>
</header>
<div class="abs hero-tag">General News, Speeches 16 December, 2016</div>
<h1 class="abs hero-title">Quis autem vel eum iure reprehenderit qui in ea voluptate velit esse quam nihil</h1>

<section class="abs content-band"></section>

<article class="abs card-dark">
  <h3>Temporibus autem quibusdam et aut officiis debitis</h3>
  <div class="mini">
    <div class="thumb" role="img" aria-label="News photo of the prince" style="background:linear-gradient(135deg,#9b8567,#4e4033)"></div>
    <p>Neque porro quisquam est qui dolorem ipsum quia dolor sit amet.<span>General News, 2016</span></p>
  </div>
  <div class="mini">
    <div class="thumb" role="img" aria-label="News photo of an official meeting" style="background:linear-gradient(135deg,#8d94a0,#3f4650)"></div>
    <p>Impedit quo minus id quod maxime placeat facere possimus.<span>General News, 2016</span></p>
  </div>
  <div class="pager"><i></i><i></i><i></i></div>
</article>

<div class="abs story" role="img" aria-label="Portrait photo of the prince in traditional dress"></div>
<div class="abs story-text">
  <h2>Main story of the week/month</h2>
  <span class="btn">More Information</span>
</div>

<aside class="abs newsletter">
  <h4>Newsletter Signup</h4>
  <p>Sign up for the latest news and stories delivered to you.</p>
  <div class="field"></div>
  <span class="btn">Subscribe</span>
</aside>
<div class="abs national">Happy National Day</div>
<aside class="abs quotes">
  <h4>Quotes by the Prince</h4>
  <p>“Our ambition is for the long term, and our future is built on what our people achieve together.”</p>
</aside>

<div class="abs projects" role="img" aria-label="Photo of the prince at a public event"></div>
<div class="abs projects-text">
  <h2>Projects of Prince Rashid</h2>
  <p>At vero eos et accusamus et iusto odio dignissimos ducimus qui blanditiis praesentium voluptatum deleniti atque corrupti quos dolores et quas molestias excepturi sint occaecati cupiditate non provident, similique sunt in culpa qui officia deserunt mollitia animi.</p>
  <span class="btn">More Information</span>
</div>

<section class="abs orgs">
  <h3>Various Organizations</h3>
  <p>Nam libero tempore, cum soluta nobis est eligendi optio cumque nihil impedit quo minus id quod maxime placeat facere possimus, omnis voluptas assumenda est.</p>
  <span class="btn">More Information</span>
</section>

<section class="abs social">
  <h3>Social Feed</h3>
  <div class="tweets">
    <div class="tweet"><div class="avatar"></div><p>We are proud of the progress made across the kingdom this year.<b>Sheikh Kareem</b></p></div>
    <div class="tweet"><div class="avatar"></div><p>Thank you to everyone who joined the celebrations today.<b>Sheikh Kareem</b></p></div>
  </div>
  <div class="dots"><i></i><i></i><i></i></div>
</section>

<section class="abs video-band"></section>
<div class="abs video" role="img" aria-label="Video still of a city skyline at dusk"></div>
<h2 class="abs video-title">Our Video</h2>
<svg class="abs play" width="130" height="130" viewBox="0 0 130 130" aria-hidden="true">
  <circle cx="65" cy="65" r="58" fill="rgba(0,0,0,.25)" stroke="#fff" stroke-width="6"/>
  <path d="M52 40 L92 65 L52 90 Z" fill="#fff"/>
</svg>

<footer class="abs site-footer"></footer>
<div class="abs fcol" style="left:100px">
  <h5>Information</h5>
  <div class="lead">Prince Rashid bin Nasser</div>
  <p>At vero eos et accusamus et iusto odio dignissimos ducimus qui blanditiis praesentium voluptatum deleniti.</p>
  <div class="lead">Sheikh Kareem</div>
  <ul><li>Introduction</li><li>About Sheikh Kareem</li><li>About the Region</li><li>Links</li></ul>
</div>
<div class="abs fcol" style="left:570px">
  <h5>About Us</h5>
  <div class="lead">Prince Rashid</div>
  <p>Similique sunt in culpa qui officia deserunt mollitia animi, id est laborum et dolorum fuga rerum.</p>
  <div class="lead">Contribution</div>
  <ul><li>The Sheikh</li><li>Awards and Achievements</li><li>Future Agenda</li><li>The Kingdom</li><li>History</li></ul>
</div>
<div class="abs fcol company" style="left:1000px">
  <h5>Company</h5>
  <ul><li>Quotes</li><li>Speeches</li><li>Foundations</li><li>Thoughts</li><li>Interviews</li><li>Articles</li><li>Gallery</li></ul>
</div>
<div class="abs footer-bar">
  <span>© 2016 COMPANY NAME. All rights reserved. Terms of Use</span>
  <span class="legal"><span>Terms &amp; Conditions</span><span>Privacy Policy</span></span>
</div>

</body>
</html>
```